Tallow Fern Studio business cards

We are a new company based in New Zealand. We Specialize in High end Luxury Residential Architecture.

Every home is bespoke and is designed to each clients individual requirements and needs.

I like to design buildings that inspire people through light and form while offering a high level of comfort and usability.

Lines of sight, proportion and balance are fundamental to the spaces I create.
Updates

August 5th is current deadline - Today's date is the 13th of August.

Target Market(s)

New Zealanders who want a custom individual home design, typically 30-65 year old males and females

Industry/Entity Type

Architecture

Contact Information for Business Card

Director - Derek Holloway
Contact Number - 0274619037
Email - info@tallowfernstudio.co.nz
Webstie - www.tallowfernstudio.co.nz
Social Media - @tallowfernstudio

Font styles to use
Sans Serif

Requirements
Must have
• Logo (Both Sides)
Website
Email
Contact Number
Social Media

Nice to have
• Texture
Should not have
• More than 3 colours - typically I would've thought 2 would be good to match the logo.

```html
<!DOCTYPE html>
<html lang="en">
<head>
<meta charset="utf-8">
<title>Tallow Fern Studio — Business Cards</title>
<link rel="stylesheet" href="https://fonts.googleapis.com/css2?family=Montserrat:wght@300;400;600&display=swap">
<style>
  :root {
    --backdrop: #202020;
    --card: #161616;
    --card-sheen: #262626;
    --silver: #b8b8b8;
    --silver-soft: #9a9a9a;
  }
  * { box-sizing: border-box; margin: 0; padding: 0; }
  html, body {
    width: 1200px; height: 900px; overflow: hidden;
    background: var(--backdrop);
    font-family: "Montserrat", sans-serif;
    color: var(--silver);
  }
  .sheet {
    width: 1200px; height: 900px;
    display: flex; flex-direction: column;
    align-items: center; justify-content: center; gap: 40px;
  }
  .card {
    width: 700px; height: 400px;
    background: linear-gradient(135deg, var(--card) 0%, var(--card) 45%, var(--card-sheen) 100%);
    position: relative;
  }
  .card--front {
    display: flex; flex-direction: column; align-items: center; justify-content: center;
  }
  .brand-mark {
    width: 46px; height: 46px; border-radius: 50%;
    border: 4px solid var(--silver); margin-bottom: 22px;
  }
  .brand-name {
    font-weight: 300; font-size: 34px; letter-spacing: 0.55em;
    padding-left: 0.55em; text-transform: uppercase;
  }
  .brand-sub {
    font-weight: 300; font-size: 11px; letter-spacing: 1.6em;
    padding-left: 1.6em; text-transform: uppercase; margin-top: 6px;
  }
  .card--back {
    display: flex; align-items: center; justify-content: center;
  }
  .identity { text-align: right; width: 300px; padding-right: 22px; }
  .identity__name {
    font-weight: 600; font-size: 30px; text-transform: uppercase; letter-spacing: 0.01em;
  }
  .identity__role { font-weight: 400; font-size: 16px; color: var(--silver-soft); margin-top: 2px; }
  .divider { width: 2px; height: 110px; background: var(--silver-soft); }
  .contacts { list-style: none; padding-left: 26px; width: 370px; }
  .contacts li {
    display: flex; align-items: center; gap: 10px;
    font-size: 17px; font-weight: 400; line-height: 1.55;
  }
  .contacts svg { width: 13px; height: 13px; flex: none; }
  .contacts svg * { fill: none; stroke: var(--silver); stroke-width: 1.6; }
</style>
</head>
<body>
<main class="sheet">
  <section class="card card--front" aria-label="Card front">
    <div class="brand-mark"></div>
    <div class="brand-name">Tallow Fern</div>
    <div class="brand-sub">Studio</div>
  </section>

  <section class="card card--back" aria-label="Card back">
    <div class="identity">
      <div class="identity__name">Derek Holloway</div>
      <div class="identity__role">Director</div>
    </div>
    <div class="divider"></div>
    <ul class="contacts">
      <li>
        <svg viewBox="0 0 16 16"><path d="M4 1.5 L6.5 4.5 L5 6.5 Q6.5 9.5 9.5 11 L11.5 9.5 L14.5 12 L12.5 14.5 Q5 13 1.5 3.5 Z"/></svg>
        0274619037
      </li>
      <li>
        <svg viewBox="0 0 16 16"><rect x="1.5" y="3.5" width="13" height="9"/><path d="M1.5 3.5 L8 9 L14.5 3.5"/></svg>
        info@tallowfernstudio.co.nz
      </li>
      <li>
        <svg viewBox="0 0 16 16"><circle cx="8" cy="8" r="6.5"/><ellipse cx="8" cy="8" rx="2.8" ry="6.5"/><path d="M1.5 8 H14.5"/></svg>
        www.tallowfernstudio.co.nz
      </li>
      <li>
        <svg viewBox="0 0 16 16"><circle cx="8" cy="8" r="5"/></svg>
        @tallowfernstudio
      </li>
    </ul>
  </section>
</main>
</body>
</html>
```